Ravelor Global Kft. is an online recruitment marketplace connecting the employers and recruiters together. We provide an e-bussiness solution for companies and give busines opportunity for recruiters.
We have a logo design already, which should be used on the business card.
Our colours are grey and magenta, which can be seen in the logo. Black is also welcome.
The style should be dynamic, young but professional. It should be clear, visible, elegant, not too crowded, simple but exciting.
We need the following data on the BC: name, title, address, phone,fax and mobile number, email address, website.
Target Market(s)
Our target market are companies, as this is a B2B business. We also target recruiters, recruitment professionals, headhunters.We would like to be impressive and different.
Industry/Entity Type
Business
Requirements
Must have
- We would like to promote our website, www.ravelorglb.hu.
- Please, put this on the back with a quite visible letter size.The style should be dynamic, young but professional. It should be clear, visible, elegant, not too crowded, simple but exciting.
Should not have
- We do not want to see people figures.

```html
<!DOCTYPE html>
<html lang="en">
<head>
<meta charset="utf-8">
<title>Ravelor Global Kft. – Business Card</title>
<link href="https://fonts.googleapis.com/css2?family=Arimo:wght@400;700&display=swap" rel="stylesheet">
<style>
  :root {
    --stage: #000000;
    --card-light: #ffffff;
    --card-edge: #dcdcde;
    --magenta: #e2007a;
    --grey: #7b7b7d;
    --text-dark: #555558;
  }
  html, body {
    margin: 0;
    padding: 0;
    width: 1200px;
    height: 900px;
    overflow: hidden;
    background: var(--stage);
    font-family: "Arimo", Arial, sans-serif;
  }
  .stage {
    position: relative;
    width: 1200px;
    height: 900px;
  }
  .card {
    position: absolute;
    left: 244px;
    width: 660px;
    height: 380px;
    border-radius: 24px;
    background: radial-gradient(ellipse at 60% 45%, var(--card-light) 0%, #f4f4f5 45%, var(--card-edge) 100%);
  }
  .card--front { top: 44px; }
  .card--back { top: 480px; }

  .contact {
    position: absolute;
    left: 40px;
    top: 102px;
    color: var(--text-dark);
  }
  .contact__name {
    margin: 0;
    font-size: 28px;
    font-weight: 400;
    letter-spacing: 3px;
    color: var(--magenta);
  }
  .contact__title {
    margin: 8px 0 0;
    font-size: 15px;
    letter-spacing: 1.5px;
    color: var(--grey);
  }
  .contact__lines {
    margin: 24px 0 0;
    font-size: 13px;
    font-weight: 700;
    line-height: 19px;
  }
  .contact__label { color: var(--magenta); margin-right: 4px; }
  .contact__address {
    margin: 16px 0 0;
    font-size: 13px;
    font-weight: 700;
    line-height: 19px;
  }

  .brand {
    position: absolute;
    display: flex;
    align-items: center;
    gap: 14px;
  }
  .card--front .brand { left: 322px; top: 132px; }
  .card--back .brand { left: 188px; top: 112px; }
  .brand__mark {
    width: 100px;
    height: 100px;
    background: var(--grey);
  }
  .card--back .brand__mark { width: 112px; height: 112px; }
  .brand__name {
    font-size: 38px;
    font-weight: 700;
    line-height: 40px;
    color: var(--magenta);
  }
  .card--back .brand__name { font-size: 42px; line-height: 44px; }

  .website {
    position: absolute;
    left: 0;
    right: 0;
    top: 344px;
    text-align: center;
    font-size: 14px;
    font-weight: 700;
    letter-spacing: 3px;
    color: var(--text-dark);
  }
  .website__domain { color: var(--magenta); }
</style>
</head>
<body>
<main class="stage">
  <section class="card card--front">
    <div class="contact">
      <h1 class="contact__name">Mara Kovin</h1>
      <p class="contact__title">President</p>
      <p class="contact__lines">
        <span class="contact__label">P</span>1300 555 017<br>
        <span class="contact__label">F</span>02 5550 1834<br>
        <span class="contact__label">E</span>info@ravelorglb.hu
      </p>
      <p class="contact__address">Level 2, 41 - 55 Marlow<br>St Fenwick Hills NSW 2090</p>
    </div>
    <div class="brand">
      <span class="brand__mark"></span>
      <span class="brand__name">Ravelor<br>Global</span>
    </div>
  </section>

  <section class="card card--back">
    <div class="brand">
      <span class="brand__mark"></span>
      <span class="brand__name">Ravelor<br>Global</span>
    </div>
    <p class="website">www.<span class="website__domain">ravelorglb</span>.hu</p>
  </section>
</main>
</body>
</html>
```